Can you create a clean, elegant and professional-looking Globe Dispatch portal design with coding?

We are looking for an initial design/concept with coding of daily Globe Dispatch portal . The design should be clean, elegant and professional-looking. We don't want anything too bleeding edge, and we would like to steer away from anything that looks too much like a blog. Please feel free to be creative. We are open to different styles, colour schemes etc. but it is important the design works with itself as a whole and has a consistent look and feel.

There should be at least one sidebar. We have found that most online newspapers are base white, blue, red, with a dash of colour, and I would like to suggest this as a starting point.

Top Navigation

I need a good looking Navigation bar with the following Categories U.S, World, Politics ,Business, Tech, Sport etc.

Key Sections in home Page

- Under that there should be a section for Top stories on the left side and a widget showing latest news on the right side

- Under that a section for Breaking news

- Under that a section for local news

- Below that I need the video section showing Top videos on the left side and list of videos on the right side

- Below that I need a sports section

- Below that US news section

- Below that Globe Dispatch

- Below that I need the Politics section

- Below that The business section

- Below that the science section

- Below that news around the web

- Below that the entertainment section

All these sections should have a top story on the left and list of stories on the right.

I need a logo designer for news portal

```html
<!DOCTYPE html>
<html lang="en">
<head>
<meta charset="utf-8">
<title>Globe Dispatch — Home</title>
<link rel="stylesheet" href="https://fonts.googleapis.com/css2?family=Lato:wght@400;700&display=swap">
<style>
:root{
  --brand-red:#e8242a;
  --accent-blue:#3d8fdc;
  --header-bg:#e4e4e4;
  --text-dark:#2b2b2b;
  --text-grey:#8a8a8a;
  --caption-bg:rgba(55,55,55,.78);
  --panel-shadow:0 1px 4px rgba(0,0,0,.16);
  --page-bg:#ffffff;
}
*{box-sizing:border-box;margin:0;padding:0}
html,body{width:928px;height:1200px;overflow:hidden;background:var(--page-bg)}
body{position:relative;font-family:'Lato',Arial,sans-serif;color:var(--text-dark)}

/* Header */
.site-header{position:absolute;left:0;top:0;width:928px;height:88px;background:var(--header-bg)}
.brand{position:absolute;left:32px;top:16px;display:flex;align-items:center;gap:8px;color:var(--brand-red);font-weight:700;font-size:27px;letter-spacing:.5px}
.brand-dot{width:14px;height:14px;border-radius:50%;background:var(--brand-red)}
.search{position:absolute;left:725px;top:25px;width:183px;height:26px;border:1px solid #cfcfcf;background:#ececec;font-size:10px;color:#888;padding:7px 6px}
.search svg{position:absolute;right:6px;top:4px}
.header-rule{position:absolute;left:32px;top:54px;width:876px;height:1px;background:var(--accent-blue)}
.main-nav{position:absolute;left:37px;top:62px;display:flex;gap:25px;font-size:16px;color:#333}
.main-nav .more{display:flex;align-items:center;gap:4px}

/* Section headings */
.section-title{position:absolute;font-size:16px;font-weight:400;text-transform:uppercase;color:#222;letter-spacing:.2px}
.section-rule{position:absolute;height:1px;background:var(--accent-blue)}
.section-rule::before{content:"";position:absolute;left:0;top:-1px;height:2px;background:var(--accent-blue);width:var(--lead,100px)}

/* Media blocks */
.media{position:absolute;overflow:hidden}
.fill-man{background:linear-gradient(100deg,#7a6756 0%,#9a846d 35%,#8e8a7c 60%,#b59a3a 100%)}
.fill-student{background:linear-gradient(100deg,#cdd6cd 0%,#8a8578 40%,#d9dfdb 70%,#b8cccb 100%)}
.fill-office{background:linear-gradient(90deg,#eef2f3 0%,#dfe5e8 45%,#d4ab86 78%,#8a6a52 100%)}
.fill-tablet{background:linear-gradient(135deg,#6f6f6f 0%,#b5b5b5 45%,#e5e5e5 70%,#8a8a8a 100%)}
.fill-thumb{background:linear-gradient(90deg,#c9b8a8 0%,#e7e7e7 50%,#b7c7d6 100%)}

.caption{position:absolute;left:0;right:0;bottom:0;background:var(--caption-bg);color:#fff}
.tag{display:inline-block;background:#fff;color:#333}
.date{color:#e4e4e4}

.hero .caption{height:74px;padding:4px 19px}
.hero .meta{font-size:11px;display:flex;align-items:center;gap:6px}
.hero .tag{width:76px;height:15px;line-height:15px;text-align:center;font-size:10px}
.hero h2{font-size:22px;font-weight:700;line-height:27px;margin-top:2px;white-space:nowrap}

.slider-arrows{position:absolute;right:10px;top:18px;display:flex;gap:2px}
.slider-arrows span{width:17px;height:16px;background:#3a3a3a;display:flex;align-items:center;justify-content:center}

.feature .caption{height:59px;padding:3px 18px}
.feature .meta{font-size:11px;display:flex;gap:6px;align-items:center;height:14px}
.feature .tag{width:76px;height:13px;line-height:13px;text-align:center;font-size:10px}
.feature h3{font-size:16px;font-weight:400;line-height:19px;margin-top:1px;white-space:nowrap}

.wide .caption{height:29px;padding:3px 5px}
.wide .meta{font-size:7.5px;display:flex;gap:6px;align-items:center;padding-left:6px}
.wide .tag{padding:0 4px;height:9px;line-height:9px;font-size:7.5px}
.wide h4{font-size:10px;font-weight:400;line-height:13px;white-space:nowrap}

.tile .caption{height:32px;padding:1px 4px;background:rgba(55,55,55,.7)}
.tile .meta{font-size:7.5px;display:flex;gap:3px;align-items:center;height:9px}
.tile .tag{padding:0 2px;height:9px;line-height:9px;font-size:7.5px}
.tile h4{font-size:8.6px;font-weight:400;line-height:10.5px;text-align:justify;text-align-last:justify}

/* Sidebar lists */
.side-list{position:absolute;background:#fff;box-shadow:var(--panel-shadow);padding:9px 0 0 8px}
.side-item{display:flex;gap:6px;height:46px}
.side-item .thumb{position:relative;width:68px;height:38px;margin-top:4px;flex:none}
.side-item .thumb svg{position:absolute;left:23px;top:8px}
.side-body{width:203px}
.side-body time{display:block;font-size:5.5px;color:#999;line-height:6px}
.side-body h5{font-size:9.5px;font-weight:400;line-height:11px;border-bottom:1px solid var(--accent-blue)}
.side-body p{font-size:9px;line-height:11px;color:var(--text-grey)}
.side-body a{color:var(--accent-blue);text-decoration:none;margin-left:6px}

.band-shadow{position:absolute;left:0;width:928px;height:4px;background:linear-gradient(#f0f0f0,#fff)}
.grid-shadow{position:absolute;left:37px;width:871px;height:6px;box-shadow:0 3px 4px -2px rgba(0,0,0,.12)}

.play{position:absolute;left:249px;top:57px}
</style>
</head>
<body>

<header class="site-header">
  <div class="brand"><span class="brand-dot"></span>Globe Dispatch</div>
  <div class="search">Search Here........
    <svg width="20" height="18" viewBox="0 0 20 18"><circle cx="8" cy="7" r="5.5" fill="none" stroke="#9a9a9a" stroke-width="2"/><line x1="12" y1="11" x2="18" y2="16" stroke="#9a9a9a" stroke-width="2.5"/></svg>
  </div>
  <div class="header-rule"></div>
  <nav class="main-nav">
    <span>U.S</span><span>World</span><span>Politics</span><span>Business</span><span>Tech</span><span>Sports</span><span>Entertainment</span>
    <span class="more">More <svg width="10" height="7" viewBox="0 0 10 7"><path d="M1 1l4 4 4-4" fill="none" stroke="var(--accent-blue)" stroke-width="2"/></svg></span>
  </nav>
</header>

<!-- Top stories -->
<h2 class="section-title" style="left:37px;top:110px">Top Stories</h2>
<div class="section-rule" style="left:37px;top:129px;width:568px;--lead:100px"></div>
<h2 class="section-title" style="left:626px;top:110px">Latest</h2>
<div class="section-rule" style="left:626px;top:129px;width:282px;--lead:54px"></div>

<article class="media hero fill-man" style="left:36px;top:144px;width:567px;height:198px" role="img" aria-label="Portrait photo of a smiling man in an office">
  <div class="slider-arrows">
    <span><svg width="8" height="10" viewBox="0 0 8 10"><path d="M6 1L2 5l4 4" fill="none" stroke="#fff" stroke-width="2"/></svg></span>
    <span><svg width="8" height="10" viewBox="0 0 8 10"><path d="M2 1l4 4-4 4" fill="none" stroke="#fff" stroke-width="2"/></svg></span>
  </div>
  <div class="caption">
    <div class="meta"><span class="tag">Tag Here</span><span class="date">28-December-2016</span></div>
    <h2>Lorem Ipsum is simply dummy text of<br>the printing and typesetting industry</h2>
  </div>
</article>

<aside class="side-list" style="left:626px;top:146px;width:282px;height:196px">
  <div class="side-item"><div class="thumb fill-thumb" role="img" aria-label="News thumbnail photo"></div><div class="side-body"><time>20-Oct-2016</time><h5>Lorem Ipsum is simply dummy text</h5><p>Lorem Ipsum is simply dummy text of the printing and typesetting industry<a href="#">Read More &gt;&gt;</a></p></div></div>
  <div class="side-item"><div class="thumb fill-thumb" role="img" aria-label="News thumbnail photo"></div><div class="side-body"><time>20-Oct-2016</time><h5>Lorem Ipsum is simply dummy text</h5><p>Lorem Ipsum is simply dummy text of the printing and typesetting industry<a href="#">Read More &gt;&gt;</a></p></div></div>
  <div class="side-item"><div class="thumb fill-thumb" role="img" aria-label="News thumbnail photo"></div><div class="side-body"><time>20-Oct-2016</time><h5>Lorem Ipsum is simply dummy text</h5><p>Lorem Ipsum is simply dummy text of the printing and typesetting industry<a href="#">Read More &gt;&gt;</a></p></div></div>
  <div class="side-item"><div class="thumb fill-thumb" role="img" aria-label="News thumbnail photo"></div><div class="side-body"><time>20-Oct-2016</time><h5>Lorem Ipsum is simply dummy text</h5><p>Lorem Ipsum is simply dummy text of the printing and typesetting industry<a href="#">Read More &gt;&gt;</a></p></div></div>
</aside>

<div class="band-shadow" style="top:358px"></div>

<!-- Breaking news -->
<h2 class="section-title" style="left:37px;top:392px">Breaking News</h2>
<div class="section-rule" style="left:37px;top:412px;width:871px;--lead:132px"></div>

<article class="media feature fill-student" style="left:37px;top:425px;width:383px;height:200px" role="img" aria-label="Photo of a smiling student with a backpack">
  <div class="caption"><div class="meta"><span class="tag">Tag Here</span><span class="date">28-December-2016</span></div><h3>Lorem Ipsum is simply dummy text of the print-<br>ing</h3></div>
</article>
<article class="media wide fill-office" style="left:427px;top:425px;width:241px;height:93px" role="img" aria-label="Photo of a businesswoman in an office">
  <div class="caption"><div class="meta"><span class="tag">Tag Here</span><span class="date">28-December-2016</span></div><h4>Lorem Ipsum is simply dummy text of the print</h4></div>
</article>
<article class="media wide fill-office" style="left:427px;top:524px;width:241px;height:101px" role="img" aria-label="Photo of a businesswoman in an office">
  <div class="caption"><div class="meta"><span class="tag">Tag Here</span><span class="date">28-December-2016</span></div><h4>Lorem Ipsum is simply dummy text of the print</h4></div>
</article>
<article class="media tile fill-tablet" style="left:680px;top:425px;width:114px;height:93px" role="img" aria-label="Photo of hands using a tablet"><div class="caption"><div class="meta"><span class="tag">Tag Here</span><span class="date">28-Dec-2017</span></div><h4>Lorem Ipsum is simply<br>dummy text of the print</h4></div></article>
<article class="media tile fill-tablet" style="left:798px;top:425px;width:110px;height:93px" role="img" aria-label="Photo of hands using a tablet"><div class="caption"><div class="meta"><span class="tag">Tag Here</span><span class="date">28-Dec-2017</span></div><h4>Lorem Ipsum is simply<br>dummy text of the print</h4></div></article>
<article class="media tile fill-tablet" style="left:680px;top:524px;width:114px;height:101px" role="img" aria-label="Photo of hands using a tablet"><div class="caption"><div class="meta"><span class="tag">Tag Here</span><span class="date">28-Dec-2017</span></div><h4>Lorem Ipsum is simply<br>dummy text of the print</h4></div></article>
<article class="media tile fill-tablet" style="left:798px;top:524px;width:110px;height:101px" role="img" aria-label="Photo of hands using a tablet"><div class="caption"><div class="meta"><span class="tag">Tag Here</span><span class="date">28-Dec-2017</span></div><h4>Lorem Ipsum is simply<br>dummy text of the print</h4></div></article>
<div class="grid-shadow" style="top:633px"></div>

<!-- Local news -->
<h2 class="section-title" style="left:37px;top:671px">Local News</h2>
<div class="section-rule" style="left:37px;top:691px;width:871px;--lead:130px"></div>

<article class="media feature fill-student" style="left:37px;top:704px;width:383px;height:200px" role="img" aria-label="Photo of a smiling student with a backpack">
  <div class="caption"><div class="meta"><span class="tag">Tag Here</span><span class="date">28-December-2016</span></div><h3>Lorem Ipsum is simply dummy text of the print-<br>ing</h3></div>
</article>
<article class="media wide fill-office" style="left:427px;top:704px;width:241px;height:93px" role="img" aria-label="Photo of a businesswoman in an office">
  <div class="caption"><div class="meta"><span class="tag">Tag Here</span><span class="date">28-December-2016</span></div><h4>Lorem Ipsum is simply dummy text of the print</h4></div>
</article>
<article class="media wide fill-office" style="left:427px;top:803px;width:241px;height:101px" role="img" aria-label="Photo of a businesswoman in an office">
  <div class="caption"><div class="meta"><span class="tag">Tag Here</span><span class="date">28-December-2016</span></div><h4>Lorem Ipsum is simply dummy text of the print</h4></div>
</article>
<article class="media tile fill-tablet" style="left:680px;top:704px;width:114px;height:93px" role="img" aria-label="Photo of hands using a tablet"><div class="caption"><div class="meta"><span class="tag">Tag Here</span><span class="date">28-Dec-2017</span></div><h4>Lorem Ipsum is simply<br>dummy text of the print</h4></div></article>
<article class="media tile fill-tablet" style="left:798px;top:704px;width:110px;height:93px" role="img" aria-label="Photo of hands using a tablet"><div class="caption"><div class="meta"><span class="tag">Tag Here</span><span class="date">28-Dec-2017</span></div><h4>Lorem Ipsum is simply<br>dummy text of the print</h4></div></article>
<article class="media tile fill-tablet" style="left:680px;top:803px;width:114px;height:101px" role="img" aria-label="Photo of hands using a tablet"><div class="caption"><div class="meta"><span class="tag">Tag Here</span><span class="date">28-Dec-2017</span></div><h4>Lorem Ipsum is simply<br>dummy text of the print</h4></div></article>
<article class="media tile fill-tablet" style="left:798px;top:803px;width:110px;height:101px" role="img" aria-label="Photo of hands using a tablet"><div class="caption"><div class="meta"><span class="tag">Tag Here</span><span class="date">28-Dec-2017</span></div><h4>Lorem Ipsum is simply<br>dummy text of the print</h4></div></article>
<div class="grid-shadow" style="top:912px"></div>

<!-- Videos -->
<h2 class="section-title" style="left:39px;top:949px">Top Videos</h2>
<div class="section-rule" style="left:39px;top:969px;width:567px;--lead:98px"></div>
<h2 class="section-title" style="left:627px;top:949px">Videos List</h2>
<div class="section-rule" style="left:627px;top:969px;width:281px;--lead:90px"></div>

<article class="media hero fill-man" style="left:37px;top:983px;width:567px;height:198px" role="img" aria-label="Video still of a smiling man in an office">
  <div class="slider-arrows">
    <span><svg width="8" height="10" viewBox="0 0 8 10"><path d="M6 1L2 5l4 4" fill="none" stroke="#fff" stroke-width="2"/></svg></span>
    <span><svg width="8" height="10" viewBox="0 0 8 10"><path d="M2 1l4 4-4 4" fill="none" stroke="#fff" stroke-width="2"/></svg></span>
  </div>
  <svg class="play" width="92" height="92" viewBox="0 0 92 92"><circle cx="46" cy="46" r="43" fill="rgba(255,255,255,.08)" stroke="rgba(200,200,200,.85)" stroke-width="3"/><path d="M36 26l30 20-30 20z" fill="rgba(200,200,200,.85)"/></svg>
  <div class="caption">
    <div class="meta"><span class="tag">Tag Here</span><span class="date">28-December-2016</span></div>
    <h2>Lorem Ipsum is simply dummy text of<br>the printing and typesetting industry</h2>
  </div>
</article>

<aside class="side-list" style="left:627px;top:985px;width:281px;height:196px">
  <div class="side-item"><div class="thumb fill-thumb" role="img" aria-label="Video thumbnail"><svg width="18" height="18" viewBox="0 0 18 18"><circle cx="9" cy="9" r="8" fill="none" stroke="#333" stroke-width="1.2"/><path d="M7 5l6 4-6 4z" fill="#333"/></svg></div><div class="side-body"><time>20-Oct-2016</time><h5>Lorem Ipsum is simply dummy text</h5><p>Lorem Ipsum is simply dummy text of the printing and typesetting industry<a href="#">Read More &gt;&gt;</a></p></div></div>
  <div class="side-item"><div class="thumb fill-thumb" role="img" aria-label="Video thumbnail"><svg width="18" height="18" viewBox="0 0 18 18"><circle cx="9" cy="9" r="8" fill="none" stroke="#333" stroke-width="1.2"/><path d="M7 5l6 4-6 4z" fill="#333"/></svg></div><div class="side-body"><time>20-Oct-2016</time><h5>Lorem Ipsum is simply dummy text</h5><p>Lorem Ipsum is simply dummy text of the printing and typesetting industry<a href="#">Read More &gt;&gt;</a></p></div></div>
  <div class="side-item"><div class="thumb fill-thumb" role="img" aria-label="Video thumbnail"><svg width="18" height="18" viewBox="0 0 18 18"><circle cx="9" cy="9" r="8" fill="none" stroke="#333" stroke-width="1.2"/><path d="M7 5l6 4-6 4z" fill="#333"/></svg></div><div class="side-body"><time>20-Oct-2016</time><h5>Lorem Ipsum is simply dummy text</h5><p>Lorem Ipsum is simply dummy text of the printing and typesetting industry<a href="#">Read More &gt;&gt;</a></p></div></div>
  <div class="side-item"><div class="thumb fill-thumb" role="img" aria-label="Video thumbnail"><svg width="18" height="18" viewBox="0 0 18 18"><circle cx="9" cy="9" r="8" fill="none" stroke="#333" stroke-width="1.2"/><path d="M7 5l6 4-6 4z" fill="#333"/></svg></div><div class="side-body"><time>20-Oct-2016</time><h5>Lorem Ipsum is simply dummy text</h5><p>Lorem Ipsum is simply dummy text of the printing and typesetting industry<a href="#">Read More &gt;&gt;</a></p></div></div>
</aside>

<div class="band-shadow" style="top:1196px"></div>
</body>
</html>
```